PREMIUM AGENCY High End Business Card - A+++ Designers Wanted

** DO NOT ATTEMPT TO CONTACT ME THROUGH SEARCHING ON ZINTREL OR EMAILING ME THROUGH MY WEBSITE **

I need a fresh, contemporary business card designed using the logo attached (BRONSALK)

I have attached the font for BRONSALK

It must have a premium look and feel. The business card size must be STANDARD size.

You can submit either/both VERTICAL or HORIZONTAL designs.

FRONT: It must have the following sample information on

Paul Ardley
Director Operations
Mobile +61 452 118 906
Email paulardley@bronsalk.com
www.bronsalk.com

The REAR of the business card must have the words

CREATE INSPIRE TOMORROW

as part of the design, in the same font (NEXA) attached.

The words do not need to be in capitals, or on the same line, please design this as you see it best working.

ADDITIONAL INFORMATION
======================

The BRONSALK logo must be on the front of the card

I want Ultraviolet printing on the final design, to enhance either the NAME of the person OR the BRONSALK logo OR the words on the back of the card.

Target Market(s)

Agency, Advertising Agency, Creative, Designers

Industry/Entity Type

Media

Contact Information for Business Card

Design Agency, Contemporary, Premium look and feel, High Quality

Font styles to use
Serif
Sans Serif
Other font styles liked:
• ATTACHED TO PROJECT

Requirements
Must have
• BLACK & WHITE as the primary design, and if you feel there can be a highlighted colour, then this can be used.
• The Logo ICON attached is blue, this colour must not be changed.
• I have attached the partner brand BRONSALK MEDIA incase you need to manipulate the original files.
• ** DO NOT ATTEMPT TO CONTACT ME THROUGH SEARCHING ON ZINTREL OR EMAILING ME THROUGH MY WEBSITE **
Nice to have
• Must be Premium. I have attached some sample designs, that I like that would be a good inspiration for where this can be taken.
• My favourite design is is the KESTRAVUE2-BUSINESSCARD-TEMPLATE
Should not have
• No funny or silly standard / off the shelf designs

```html
<!DOCTYPE html>
<html lang="en">
<head>
<meta charset="utf-8">
<title>Bronsalk Business Card</title>
<link href="https://fonts.googleapis.com/css2?family=Montserrat:wght@600;700&family=Open+Sans:wght@400;600&display=swap" rel="stylesheet">
<style>
  :root {
    --backdrop: #2b2b2c;
    --card: #141415;
    --card-edge: #1d1d1f;
    --ink: #f4f4f4;
    --ink-soft: #d9d9d9;
    --ink-muted: #5c5c60;
    --brand-blue: #29a8e0;
    --divider: #1f1f21;
  }
  * { box-sizing: border-box; margin: 0; padding: 0; }
  html, body {
    width: 1200px; height: 900px; overflow: hidden;
    background: var(--backdrop);
  }
  .stage {
    position: relative; width: 1200px; height: 900px;
    display: flex; align-items: center; justify-content: center; gap: 40px;
  }
  .card {
    position: relative; width: 500px; height: 286px;
    background: var(--card);
    border-radius: 16px;
    box-shadow: 0 0 0 1px var(--card-edge), 0 18px 40px rgba(0,0,0,.45);
    overflow: hidden;
  }

  /* Front */
  .card-front { display: flex; }
  .front-brand {
    width: 250px; height: 100%;
    display: flex; align-items: center; justify-content: center; gap: 10px;
    border-right: 1px solid var(--divider);
  }
  .brand-dot {
    width: 14px; height: 14px; border-radius: 50%;
    background: var(--brand-blue); flex: none;
  }
  .brand-name {
    font-family: "Montserrat", sans-serif; font-weight: 700;
    font-size: 26px; letter-spacing: 1px; color: var(--brand-blue);
    white-space: nowrap;
  }
  .front-contact {
    padding: 84px 0 0 24px;
    font-family: "Open Sans", sans-serif;
  }
  .person-name {
    font-family: "Montserrat", sans-serif; font-weight: 600;
    font-size: 18px; color: var(--brand-blue);
  }
  .person-role { font-size: 12px; color: var(--ink-soft); margin: 2px 0 14px; }
  .contact-list { list-style: none; }
  .contact-item {
    display: flex; align-items: center; gap: 9px;
    font-size: 12.5px; color: var(--ink); line-height: 20px;
  }
  .contact-item svg { width: 10px; height: 10px; fill: var(--brand-blue); flex: none; }

  /* Back */
  .card-back {
    display: flex; flex-direction: column; justify-content: space-between;
    padding: 40px 40px 56px 90px;
  }
  .tagline {
    font-family: "Montserrat", sans-serif; font-weight: 600;
    font-size: 14px; line-height: 22px; letter-spacing: 4px;
    color: var(--ink-muted);
    text-transform: uppercase; white-space: nowrap;
  }
  .back-brand { display: flex; align-items: center; gap: 14px; }
  .back-brand .brand-name { color: var(--ink); font-size: 32px; letter-spacing: 2px; }
</style>
</head>
<body>
<main class="stage">
  <section class="card card-front" aria-label="Business card front">
    <div class="front-brand">
      <span class="brand-dot"></span>
      <span class="brand-name">BRONSALK</span>
    </div>
    <div class="front-contact">
      <p class="person-name">Paul Ardley</p>
      <p class="person-role">Director Operations</p>
      <ul class="contact-list">
        <li class="contact-item">
          <svg viewBox="0 0 10 10" aria-hidden="true"><path d="M2 0.5 L3.6 2.6 L2.8 3.6 Q4 6 6.4 7.2 L7.4 6.4 L9.5 8 L8.4 9.5 Q3 9 0.5 1.6 Z"/></svg>
          <span>+61 452 118 906</span>
        </li>
        <li class="contact-item">
          <svg viewBox="0 0 10 10" aria-hidden="true"><path d="M0.5 2 H9.5 V8.5 H0.5 Z M1 2.4 L5 5.4 L9 2.4" stroke="#141415" stroke-width="0.8"/></svg>
          <span>paulardley@bronsalk.com</span>
        </li>
        <li class="contact-item">
          <svg viewBox="0 0 10 10" aria-hidden="true"><circle cx="5" cy="5" r="4.5"/><path d="M0.5 5 H9.5 M5 0.5 Q2.5 5 5 9.5 M5 0.5 Q7.5 5 5 9.5" stroke="#141415" stroke-width="0.7" fill="none"/></svg>
          <span>www.bronsalk.com</span>
        </li>
      </ul>
    </div>
  </section>

  <section class="card card-back" aria-label="Business card back">
    <p class="tagline">Create · Inspire · Tomorrow</p>
    <div class="back-brand">
      <span class="brand-dot"></span>
      <span class="brand-name">BRONSALK</span>
    </div>
  </section>
</main>
</body>
</html>
```